Business Card Vespalor - Accounting firm

Hi my friend.
I'm coming back to you to see if it would be possible for you to make a modern and minimalist business card design.
In shades of blue like the great logo you offered me.
The ideal is a modern and aesthetic business card.
The goal is to give a professional effect to the first exchanges.
Renewal and innovation in the accounting world !!
I thank you !!
Good evening to you

Target Market(s)

Young, dynamic and sensitive to marketing

Industry/Entity Type

Finance And Accounting

Contact Information for Business Card

Company logo and name. Last name, First name, Phone number, email address, company address, website.

Font styles to use
Sans Serif

Requirements
Must have
• The ideal is a modern and aesthetic business card.

Mentions to include: Company logo and name. Last name, First name, Phone number, email address, company address, website.
Nice to have
• The goal is to give a professional effect to the first exchanges.
Should not have
• Simplistic or childish design

```html
<!DOCTYPE html>
<html lang="en">
<head>
<meta charset="utf-8">
<title>Vespalor Business Card</title>
<link rel="stylesheet" href="https://fonts.googleapis.com/css2?family=Open+Sans:ital,wght@0,400;0,600;0,700;1,400&display=swap">
<style>
  :root {
    --navy: #1f2b62;
    --teal: #2fb3b8;
    --blue: #1b7fc4;
    --ink: #2b2f3a;
    --paper: #ffffff;
    --stage: #2a2a2c;
  }
  * { margin: 0; padding: 0; box-sizing: border-box; }
  html, body { width: 1200px; height: 900px; overflow: hidden; }
  body {
    background: var(--stage);
    font-family: "Open Sans", sans-serif;
    position: relative;
  }
  .card {
    position: absolute;
    left: 280px;
    width: 640px;
    height: 366px;
    border-radius: 4px;
    box-shadow: 0 10px 30px rgba(0,0,0,.45);
    overflow: hidden;
  }
  .card--front { top: 64px; background: var(--paper); }
  .card--back { top: 470px; background: var(--navy); }

  .brand { position: absolute; display: flex; flex-direction: column; }
  .brand__row { display: flex; align-items: center; gap: 14px; }
  .brand__dot { width: 30px; height: 30px; border-radius: 50%; }
  .brand__name { font-weight: 700; line-height: 1; letter-spacing: -1px; }
  .brand__tag {
    font-size: 11px; letter-spacing: 7px; text-transform: uppercase;
    margin-top: 6px; font-weight: 400;
  }

  .card--front .brand { left: 48px; top: 42px; }
  .card--front .brand__dot { background: var(--teal); }
  .card--front .brand__name { font-size: 62px; color: var(--teal); }
  .card--front .brand__tag { color: var(--navy); margin-left: 44px; }

  .divider {
    position: absolute; left: 48px; right: 48px; top: 200px;
    height: 1.5px; background: var(--blue);
  }
  .person { position: absolute; right: 48px; top: 136px; text-align: right; }
  .person__name {
    font-weight: 700; font-size: 22px; letter-spacing: .5px;
    text-transform: uppercase; color: var(--teal);
  }
  .person__role { font-size: 17px; color: var(--ink); }

  .contacts {
    position: absolute; left: 48px; top: 222px; list-style: none;
    font-size: 17px; color: var(--ink); line-height: 1.45;
  }
  .contacts li { display: flex; align-items: center; gap: 10px; }
  .contacts svg { width: 15px; height: 15px; flex: none; }

  .address {
    position: absolute; right: 48px; top: 222px; text-align: right;
    font-size: 17px; color: var(--ink); line-height: 1.45; font-style: normal;
  }

  .card--back .brand { left: 170px; top: 96px; }
  .card--back .brand__dot { background: var(--teal); }
  .card--back .brand__name { font-size: 72px; color: #ffffff; }
  .card--back .brand__tag { color: #ffffff; margin-left: 46px; }
  .tagline {
    position: absolute; left: 110px; top: 232px;
    color: #ffffff; font-style: italic; font-size: 16px; line-height: 1.5;
  }
</style>
</head>
<body>
  <section class="card card--front" aria-label="Business card front">
    <div class="brand">
      <div class="brand__row">
        <span class="brand__dot"></span>
        <span class="brand__name">Vespalor</span>
      </div>
      <span class="brand__tag">Expert-Comptable</span>
    </div>

    <div class="person">
      <p class="person__name">Dan Corvell</p>
      <p class="person__role">President</p>
    </div>

    <div class="divider"></div>

    <ul class="contacts">
      <li>
        <svg viewBox="0 0 16 16" aria-hidden="true"><path fill="#1b7fc4" d="M4 1l3 3-2 2c1 2 3 4 5 5l2-2 3 3-2 3C7 15 1 9 1 3z"/></svg>
        555-318-7042
      </li>
      <li>
        <svg viewBox="0 0 16 16" aria-hidden="true"><rect x="1" y="3" width="14" height="10" rx="1" fill="#1b7fc4"/><path d="M1 4l7 5 7-5" stroke="#fff" stroke-width="1.3" fill="none"/></svg>
        dcorvell@vespalor.com
      </li>
      <li>
        <svg viewBox="0 0 16 16" aria-hidden="true"><circle cx="8" cy="8" r="7" fill="#1b7fc4"/><path d="M1 8h14M8 1c-3 3-3 11 0 14M8 1c3 3 3 11 0 14" stroke="#fff" stroke-width="1" fill="none"/></svg>
        www.vespalor.com
      </li>
    </ul>

    <address class="address">
      1870 Harbor Crest Lane<br>
      Bayview CA 90210
    </address>
  </section>

  <section class="card card--back" aria-label="Business card back">
    <div class="brand">
      <div class="brand__row">
        <span class="brand__dot"></span>
        <span class="brand__name">Vespalor</span>
      </div>
      <span class="brand__tag">Expert-Comptable</span>
    </div>
    <p class="tagline">
      The goal is to give a professional effect to the first exchanges.<br>
      Renewal and innovation in the accounting world !!
    </p>
  </section>
</body>
</html>
```